4' x 8' Construction Project Sign, think of a very large business card

We need project signs for our construction sites, the sign will be mounted along the road so cars driving by can quickly read. the sign should be able to be read as cars drive by doing highway speed.

Think like your making a large business card

I would like to include "NOW HIRING" Superintendents, Project Managers, Pipe Foremen, Pipe Layers, and Equipment Operators

Description of services we provide should include

Civil Construction Services
Land Clearing
Excavation
Underground Utilities
Environmental Maintenance

The 2 objectives is to market to future clients and to recruit new employees

The sign will be mounted on posts at the entrance of our construction projects
Updates

Low design quality

Target Market(s)

Construction and land developers

Industry/Entity Type

Construction Company

Other font styles liked:
• Hypatia Sans Pro lite

Colors

Designer to choose colors to be used in the design.

Requirements
Must have
• Clean and easy to read
• Civil Construction Services
• Land Clearing
• Excavation
• Underground Utilities
• Road Construction

```html
<!DOCTYPE html>
<html lang="en">
<head>
<meta charset="utf-8">
<title>Harlow Brothers Civil Construction – Project Sign</title>
<link rel="stylesheet" href="https://fonts.googleapis.com/css2?family=Jost:wght@300;400&display=swap">
<style>
  :root {
    --brand-blue: #3b4799;
    --paper: #ffffff;
    --frame: #cfcfcf;
  }
  html, body {
    margin: 0;
    padding: 0;
    overflow: hidden;
    background: var(--paper);
  }
  .sign {
    position: relative;
    width: 1200px;
    height: 1200px;
    background: var(--paper);
    overflow: hidden;
    font-family: "Jost", sans-serif;
    font-weight: 300;
  }
  .sign__frame {
    position: absolute;
    left: 56px;
    top: 56px;
    width: 1094px;
    height: 1094px;
    border: 1px solid var(--frame);
    box-sizing: border-box;
  }
  .brand__square {
    position: absolute;
    left: 134px;
    top: 126px;
    width: 74px;
    height: 76px;
    background: var(--brand-blue);
  }
  .brand__divider {
    position: absolute;
    left: 223px;
    top: 115px;
    width: 3px;
    height: 98px;
    background: #a3a3a3;
  }
  .brand__name {
    position: absolute;
    left: 236px;
    top: 126px;
    margin: 0;
    color: var(--brand-blue);
    font-weight: 400;
    line-height: 1;
  }
  .brand__name-main {
    display: block;
    font-size: 37px;
    letter-spacing: 0.5px;
  }
  .brand__name-sub {
    display: block;
    margin-top: 9px;
    font-size: 19px;
    letter-spacing: 9.4px;
  }
  .hiring-band {
    position: absolute;
    left: 219px;
    top: 225px;
    width: 931px;
    height: 122px;
    background: var(--brand-blue);
  }
  .hiring-band__title {
    position: absolute;
    left: 36px;
    top: 10px;
    margin: 0;
    color: var(--paper);
    font-size: 98px;
    font-weight: 300;
    letter-spacing: 30px;
    line-height: 100px;
    white-space: nowrap;
  }
  .positions {
    position: absolute;
    left: 246px;
    top: 368px;
    margin: 0;
    color: var(--brand-blue);
    font-size: 61px;
    line-height: 60.5px;
    font-weight: 300;
  }
  .services-band {
    position: absolute;
    left: 219px;
    top: 581px;
    width: 931px;
    height: 569px;
    background: var(--brand-blue);
  }
  .services {
    list-style: none;
    position: absolute;
    left: 32px;
    top: 60px;
    margin: 0;
    padding: 0;
    color: var(--paper);
    font-size: 78px;
    line-height: 86.5px;
    font-weight: 300;
    white-space: nowrap;
  }
</style>
</head>
<body>
  <main class="sign">
    <div class="sign__frame"></div>

    <header class="brand">
      <div class="brand__square"></div>
      <div class="brand__divider"></div>
      <h1 class="brand__name">
        <span class="brand__name-main">HARLOW BROTHERS</span>
        <span class="brand__name-sub">CIVIL CONSTRUCTION</span>
      </h1>
    </header>

    <section class="hiring-band">
      <h2 class="hiring-band__title">NOW HIRING</h2>
    </section>

    <p class="positions">Superintendents, project managers<br>pipe foremen, pipe layers and<br>equipment operators</p>

    <section class="services-band">
      <ul class="services">
        <li>Civil Construction Services</li>
        <li>Land Clearing</li>
        <li>Excavation</li>
        <li>Underground Utilities</li>
        <li>Environmental Maintenance</li>
      </ul>
    </section>
  </main>
</body>
</html>
```